GDFH Business Card

Looking for a business card design to incorporate our branding. We want to only use the colors listing in the Branding Package (attached).
Updates

Target Market(s)

People who need their phone or device fixed.

Industry/Entity Type

Electronics

Contact Information for Business Card

Please use:

Gadget Fix Haven LLC
4870 S Ridgecrest Pkwy
Suite 318
San Antonio, TX 78291

Wendell Thorsby, Store Manager

(210) 555-0147

Requirements
Must have
• Must include the colors that are contained within the Branding Package PDF file.

```html
<!DOCTYPE html>
<html lang="en">
<head>
<meta charset="utf-8">
<title>Gadget Fix Haven – Business Card</title>
<link rel="stylesheet" href="https://fonts.googleapis.com/css2?family=Questrial&family=Poppins:wght@500&display=swap">
<style>
  :root {
    --stage: #d9d4cc;
    --card-light: #f4f3f1;
    --card-mid: #e2e1df;
    --brand-red: #d4321f;
    --brand-red-deep: #b3200f;
    --brand-red-bright: #e8452c;
    --charcoal: #3a3c42;
    --ink: #1c1c1c;
    --on-red: rgba(255, 255, 255, 0.86);
    --on-red-soft: rgba(255, 255, 255, 0.72);
  }
  * { margin: 0; padding: 0; box-sizing: border-box; }
  html, body {
    width: 1200px;
    height: 970px;
    overflow: hidden;
    background: var(--stage);
  }
  .business-card {
    position: absolute;
    left: 80px;
    top: 190px;
    width: 1040px;
    height: 590px;
    border-radius: 30px;
    overflow: hidden;
    background: linear-gradient(160deg, var(--card-light) 0%, #ffffff 45%, var(--card-mid) 100%);
    box-shadow: 0 18px 40px rgba(0, 0, 0, 0.22);
    font-family: "Questrial", "Century Gothic", sans-serif;
  }
  .card-waves {
    position: absolute;
    inset: 0;
    width: 100%;
    height: 100%;
  }
  .brand-lockup {
    position: absolute;
    left: 53px;
    top: 88px;
    display: flex;
    align-items: center;
    gap: 30px;
  }
  .brand-square {
    width: 117px;
    height: 117px;
    border-radius: 14px;
    background: var(--brand-red);
  }
  .brand-name {
    font-size: 58px;
    color: var(--brand-red);
    letter-spacing: -0.5px;
    line-height: 1;
  }
  .contact-person {
    position: absolute;
    left: 53px;
    top: 428px;
    color: var(--on-red);
  }
  .person-name {
    font-family: "Poppins", "Century Gothic", sans-serif;
    font-weight: 500;
    font-size: 29px;
    line-height: 1.1;
  }
  .person-role {
    font-size: 25px;
    color: var(--on-red-soft);
    line-height: 1.2;
  }
  .person-phone {
    display: flex;
    align-items: center;
    gap: 14px;
    margin-top: 20px;
    font-size: 27px;
    color: var(--on-red-soft);
  }
  .phone-icon { width: 30px; height: 30px; }
  .company-block {
    position: absolute;
    right: 47px;
    top: 430px;
    width: 430px;
    color: var(--on-red);
  }
  .company-name {
    font-size: 30px;
    line-height: 1.1;
    margin-bottom: 16px;
  }
  .company-address {
    font-size: 26px;
    font-style: normal;
    line-height: 1.36;
    color: var(--on-red-soft);
  }
</style>
</head>
<body>
  <div class="business-card">
    <svg class="card-waves" viewBox="0 0 1040 590" preserveAspectRatio="none" aria-hidden="true">
      <defs>
        <linearGradient id="red-field" x1="0" y1="0" x2="1" y2="1">
          <stop offset="0" stop-color="var(--brand-red-deep)"/>
          <stop offset="0.4" stop-color="var(--brand-red-bright)"/>
          <stop offset="1" stop-color="var(--brand-red-deep)"/>
        </linearGradient>
      </defs>
      <path fill="var(--charcoal)" d="M0,335 C200,285 450,295 620,332 C800,372 960,345 1040,172 L1040,348 C800,382 420,300 0,358 Z"/>
      <path fill="#ffffff" opacity="0.9" d="M0,356 C300,312 600,322 800,356 C900,372 990,364 1040,347 L1040,356 C990,372 900,380 800,364 C600,330 300,320 0,364 Z"/>
      <path fill="url(#red-field)" d="M0,364 C300,320 600,330 800,364 C900,380 990,372 1040,356 L1040,590 L0,590 Z"/>
    </svg>

    <div class="brand-lockup">
      <div class="brand-square"></div>
      <div class="brand-name">Gadget Fix Haven</div>
    </div>

    <div class="contact-person">
      <div class="person-name">Wendell Thorsby</div>
      <div class="person-role">Store Manager</div>
      <div class="person-phone">
        <svg class="phone-icon" viewBox="0 0 30 30" aria-hidden="true">
          <rect x="1" y="1" width="28" height="28" rx="5" fill="rgba(255,255,255,0.75)"/>
          <path d="M7,11 C7,8 23,8 23,11 L21,13 L18,12 L18,10 C16,9.5 14,9.5 12,10 L12,12 L9,13 Z" fill="var(--brand-red)"/>
          <rect x="9" y="15" width="12" height="9" rx="2" fill="var(--brand-red)"/>
          <circle cx="15" cy="19.5" r="2.2" fill="rgba(255,255,255,0.8)"/>
        </svg>
        <span>(210) 555-0147</span>
      </div>
    </div>

    <div class="company-block">
      <div class="company-name">Gadget Fix Haven LLC</div>
      <address class="company-address">
        4870 S Ridgecrest Pkwy<br>
        Suite 318, San Antonio, TX 78291
      </address>
    </div>
  </div>
</body>
</html>
```